Medical Practice Business Card

we need a business card for our new medical ophthalmology practice based in Needham Massachusetts. we are looking for a simple , modern and elegant design.
the card needs to contain the following
1- the logo of our practice (please see attached file)
2- the name of the practice : "Silver Birch Retina Care"
3- Doctor's Name: Tobias Rendell MD PhD
4- Specialty: Board-Certified Vitreoretinal Surgeon
5- practice address: 87 Larkspur Ave, Suite 210, Needham MA 02481
7- Office number: 617- 482 - 7730
8- fax number: 617- 391 - 2268
9- email: info@sbretinahub.example
10- website: www.sbretinahub.example

```html
<!DOCTYPE html>
<html lang="en">
<head>
<meta charset="utf-8">
<title>Silver Birch Retina Care – Business Card</title>
<link rel="stylesheet" href="https://fonts.googleapis.com/css2?family=Arimo:wght@400;700&display=swap">
<style>
  :root {
    --navy: #143a63;
    --navy-deep: #0f2c4c;
    --blue-glow: #2c74ad;
    --accent-blue: #2a6fb3;
    --teal: #3fc4c4;
    --teal-light: #7fd8e0;
    --ink: #1c2333;
    --paper: #ffffff;
    --stage: #e9ecef;
    --divider: #c9ccd1;
  }
  * { box-sizing: border-box; margin: 0; padding: 0; }
  html, body { width: 1200px; height: 779px; overflow: hidden; }
  body {
    background: var(--stage);
    display: flex;
    align-items: center;
    justify-content: center;
    gap: 40px;
    font-family: "Arimo", Arial, sans-serif;
  }
  .card {
    position: relative;
    width: 540px;
    height: 309px;
    border-radius: 18px;
    overflow: hidden;
    box-shadow: 0 4px 0 var(--teal), 0 10px 24px rgba(0,0,0,.18);
  }
  .brand {
    font-family: "Arimo", Arial, sans-serif;
    font-weight: 700;
    line-height: 1.15;
  }
  /* Front */
  .card--front {
    background: radial-gradient(ellipse at 55% 30%, var(--blue-glow) 0%, var(--navy) 55%, var(--navy-deep) 100%);
    color: var(--paper);
    display: flex;
    flex-direction: column;
    align-items: center;
    justify-content: center;
  }
  .card--front .brand { font-size: 36px; text-align: center; color: var(--paper); }
  .front__url {
    margin-top: 36px;
    font-size: 13px;
    letter-spacing: 3px;
  }
  /* Back */
  .card--back { background: var(--paper); color: var(--ink); }
  .back__logo {
    position: absolute;
    left: 34px; top: 108px;
    width: 210px;
  }
  .card--back .brand { color: var(--navy); font-size: 22px; }
  .back__divider {
    position: absolute;
    left: 262px; top: 46px;
    width: 1px; height: 140px;
    background: var(--divider);
  }
  .contact {
    position: absolute;
    left: 284px; top: 44px;
    font-size: 12.5px;
    line-height: 1.35;
  }
  .contact__name {
    font-weight: 700;
    font-size: 14px;
    letter-spacing: .5px;
    text-transform: uppercase;
    color: var(--navy);
  }
  .contact__role { color: var(--accent-blue); font-size: 12px; margin-bottom: 8px; }
  .contact__address { margin-bottom: 8px; }
  .contact__list { list-style: none; }
  .contact__list li { display: flex; align-items: center; gap: 7px; }
  .contact__list svg { width: 11px; height: 11px; fill: var(--navy); flex: none; }
  .back__band { position: absolute; left: 0; bottom: 0; width: 540px; height: 130px; }
</style>
</head>
<body>
  <section class="card card--front">
    <p class="brand">Silver Birch<br>Retina Care</p>
    <p class="front__url">www.sbretinahub.example</p>
  </section>

  <section class="card card--back">
    <div class="back__logo">
      <p class="brand">Silver Birch<br>Retina Care</p>
    </div>
    <div class="back__divider"></div>
    <div class="contact">
      <p class="contact__name">Tobias Rendell MD PhD</p>
      <p class="contact__role">Board-Certified Vitreoretinal Surgeon</p>
      <p class="contact__address">87 Larkspur Ave, Suite 210<br>Needham MA 02481</p>
      <ul class="contact__list">
        <li><svg viewBox="0 0 24 24"><path d="M6.6 10.8a15 15 0 0 0 6.6 6.6l2.2-2.2a1 1 0 0 1 1-.25 11.4 11.4 0 0 0 3.6.6 1 1 0 0 1 1 1V20a1 1 0 0 1-1 1A17 17 0 0 1 3 4a1 1 0 0 1 1-1h3.5a1 1 0 0 1 1 1c0 1.25.2 2.45.57 3.57a1 1 0 0 1-.25 1z"/></svg>617- 482 - 7730</li>
        <li><svg viewBox="0 0 24 24"><path d="M6 2h12v6H6zM4 9h16a2 2 0 0 1 2 2v6h-4v5H6v-5H2v-6a2 2 0 0 1 2-2zm4 8v3h8v-3z"/></svg>617- 391 - 2268</li>
        <li><svg viewBox="0 0 24 24"><path d="M2 5h20v14H2zm2 2v.4l8 5 8-5V7z"/></svg>info@sbretinahub.example</li>
        <li><svg viewBox="0 0 24 24"><path d="M12 2a10 10 0 1 0 0 20 10 10 0 0 0 0-20zm-1 17.9A8 8 0 0 1 4.1 11H8c.2 3.2 1.3 6.3 3 8.9zm0-10.9H8.1A13 13 0 0 1 11 4.1zm2 0V4.1A13 13 0 0 1 15.9 9zm0 2h3c-.2 3.2-1.3 6.3-3 8.9zm5 0h1.9a8 8 0 0 1-4.1 6.6A15 15 0 0 0 18 11zm1.9-2H18a15 15 0 0 0-2.3-6.6A8 8 0 0 1 19.9 9z"/></svg>www.sbretinahub.example</li>
      </ul>
    </div>
    <svg class="back__band" viewBox="0 0 540 130" preserveAspectRatio="none">
      <path d="M0 130 L0 118 Q270 100 540 4 L540 130 Z" fill="var(--navy)"/>
      <path d="M0 118 Q270 100 540 4" fill="none" stroke="var(--accent-blue)" stroke-width="3"/>
      <path d="M0 124 Q270 110 540 16" fill="none" stroke="var(--teal)" stroke-width="2"/>
      <circle cx="16" cy="116" r="10" fill="var(--teal-light)"/>
    </svg>
  </section>
</body>
</html>
```